Velisto Events Business Card

We need a business cards that stands out to our clients. We are company who targets prestige clients to spend money with us on experiences, so our image needs to be prestige
Target Market(s)
Corporate
Contact Information for Business Card
There will be four different names on the business cards
Dana Morrowby
Director
O: 02 5147 3086
M: 0451 692 038
E: info@velistoevents.example.au
Facebook: @velistoevents
Instagram: velistoevents
www.velistoevents.example.au
Nathaniel Morrowby
Director
O: 02 5147 3086
M: 0467 215 904
Facebook: @velistoevents
Instagram: velistoevents
www.velistoevents.example.au
Teodor Vinkel
Director
O: 02 5147 3086
M: 0478 903 527
Facebook: @velistoevents
Instagram: velistoevents
www.velistoevents.example.au
Mabel Hartung
Director
O: 02 5147 3086
Facebook: @velistoevents
Instagram: velistoevents
www.velistoevents.example.au
Colors
Designer to choose colors to be used in the design.
Look and feel

```html
<!DOCTYPE html>
<html lang="en">
<head>
<meta charset="utf-8">
<title>Velisto Events – Business Card</title>
<link rel="stylesheet" href="https://fonts.googleapis.com/css2?family=Cinzel:wght@400;500&family=Merriweather:wght@700&family=Lora:wght@400&display=swap">
<style>
  :root {
    --backdrop: #5e4a31;
    --card-black: #030303;
    --card-panel: #141414;
    --gold: #d6b15c;
    --gold-light: #f6df97;
    --gold-dark: #a57e2c;
    --ink-white: #f4f1ea;
  }
  * { margin: 0; padding: 0; box-sizing: border-box; }
  html, body { width: 1189px; height: 1200px; overflow: hidden; }
  body { background: var(--backdrop); position: relative; }

  .card {
    position: absolute;
    left: 169px;
    width: 851px;
    height: 485px;
    border-radius: 28px;
    background: var(--card-black);
    overflow: hidden;
    box-shadow: 0 10px 24px rgba(0,0,0,.45);
  }
  .card--front { top: 112px; }
  .card--back { top: 641px; }

  .card__panel {
    position: absolute; left: 0; right: 0;
    background:
      radial-gradient(circle at 50% 50%, #1d1d1d 0%, var(--card-panel) 60%, #0c0c0c 100%);
  }
  .card--front .card__panel { top: 113px; height: 257px; }
  .card--back .card__panel { top: 53px; height: 377px; }

  .gold-rule {
    position: absolute; left: 0; right: 0; height: 5px;
    background: linear-gradient(90deg, var(--gold-dark), var(--gold) 30%, var(--gold-light) 55%, var(--gold) 75%, var(--gold-dark));
  }
  .card--front .gold-rule--top { top: 110px; }
  .card--front .gold-rule--bottom { top: 368px; }
  .card--back .gold-rule--top { top: 50px; }
  .card--back .gold-rule--bottom { top: 428px; }

  .wordmark {
    position: absolute; left: 0; right: 0; text-align: center;
    font-family: "Cinzel", serif; font-weight: 400; color: var(--gold);
    white-space: nowrap;
  }
  .wordmark__name { display: block; }
  .wordmark__sub { display: block; }

  .card--front .wordmark { top: 170px; }
  .card--front .wordmark__name { font-size: 72px; letter-spacing: 26px; line-height: 90px; padding-left: 26px; }
  .card--front .wordmark__sub { font-size: 38px; letter-spacing: 18px; line-height: 52px; padding-left: 18px; }

  .contact {
    position: absolute; left: 44px; width: 350px; top: 124px; text-align: center;
  }
  .contact .wordmark { position: static; }
  .contact .wordmark__name { font-size: 42px; letter-spacing: 13px; line-height: 48px; padding-left: 13px; }
  .contact .wordmark__sub { font-size: 22px; letter-spacing: 9px; line-height: 28px; padding-left: 9px; }

  .contact__name {
    margin-top: 10px;
    font-family: "Merriweather", serif; font-weight: 700;
    font-size: 26px; line-height: 30px; color: var(--gold);
  }
  .contact__role {
    font-family: "Lora", serif; font-size: 21px; line-height: 24px; color: var(--ink-white);
  }
  .contact__lines { margin-top: 20px; }
  .contact__line {
    display: flex; align-items: center; justify-content: center; gap: 9px;
    font-family: "Lora", serif; font-size: 19px; line-height: 31px; color: var(--ink-white);
    white-space: nowrap;
  }
  .contact__icon { width: 16px; height: 16px; flex: none; }
  .contact__web {
    margin-top: 14px;
    font-family: "Lora", serif; font-size: 18px; letter-spacing: 3.5px;
    color: var(--gold); white-space: nowrap;
  }

  .brand-seal {
    position: absolute; left: 503px; top: 140px; width: 240px; text-align: center;
  }
  .brand-seal__circle {
    width: 120px; height: 120px; margin: 0 auto 18px;
    border: 4px solid var(--gold); border-radius: 50%;
  }
  .brand-seal__name {
    font-family: "Cinzel", serif; font-weight: 400; font-size: 34px;
    letter-spacing: 8px; padding-left: 8px; color: var(--gold);
  }
</style>
</head>
<body>

<section class="card card--front" aria-label="Card front">
  <div class="card__panel"></div>
  <div class="gold-rule gold-rule--top"></div>
  <div class="gold-rule gold-rule--bottom"></div>
  <h1 class="wordmark">
    <span class="wordmark__name">VELISTO</span>
    <span class="wordmark__sub">EVENTS</span>
  </h1>
</section>

<section class="card card--back" aria-label="Card back">
  <div class="card__panel"></div>
  <div class="gold-rule gold-rule--top"></div>
  <div class="gold-rule gold-rule--bottom"></div>

  <div class="contact">
    <div class="wordmark">
      <span class="wordmark__name">VELISTO</span>
      <span class="wordmark__sub">EVENTS</span>
    </div>
    <p class="contact__name">Dana Morrowby</p>
    <p class="contact__role">Director</p>
    <div class="contact__lines">
      <p class="contact__line">
        <svg class="contact__icon" viewBox="0 0 24 24" aria-hidden="true"><path fill="#d6b15c" d="M6.6 10.8c1.4 2.8 3.8 5.1 6.6 6.6l2.2-2.2c.3-.3.7-.4 1-.2 1.1.4 2.3.6 3.6.6.6 0 1 .4 1 1V20c0 .6-.4 1-1 1C10.6 21 3 13.4 3 4c0-.6.4-1 1-1h3.5c.6 0 1 .4 1 1 0 1.3.2 2.5.6 3.6.1.3 0 .7-.2 1z"/></svg>
        <span>02 5147 3086</span>
      </p>
      <p class="contact__line">
        <svg class="contact__icon" viewBox="0 0 24 24" aria-hidden="true"><rect x="2" y="5" width="20" height="14" rx="1.5" fill="#d6b15c"/><path d="M3 6l9 7 9-7" fill="none" stroke="#141414" stroke-width="1.8"/></svg>
        <span>info@velistoevents.example.au</span>
      </p>
    </div>
    <p class="contact__web">www.velistoevents.example.au</p>
  </div>

  <div class="brand-seal">
    <div class="brand-seal__circle"></div>
    <p class="brand-seal__name">VELISTO</p>
  </div>
</section>

</body>
</html>
```